New business stationairy

I need paper with header and footer and business cards.
I am a Ltd Company and my main field of expertise is QA/QC inspection in the Oil and Gas Industry. I will need all contact detail inserted and a footer with registration number and bank details etc

Industry/Entity Type

Business

```html
<!DOCTYPE html>
<html lang="en">
<head>
<meta charset="utf-8">
<title>Marlowe Inspection Services Ltd. – Letterhead</title>
<link href="https://fonts.googleapis.com/css2?family=Montserrat:wght@300;400;600;700&display=swap" rel="stylesheet">
<style>
  :root {
    --backdrop: #e9e9ea;
    --paper: #ffffff;
    --slate: #78777c;
    --petrol: #1e5e80;
    --ink: #5a5a5e;
    --light: #ffffff;
  }
  * { margin: 0; padding: 0; box-sizing: border-box; }
  html, body {
    width: 1200px;
    height: 936px;
    overflow: hidden;
    background: var(--backdrop);
    font-family: "Montserrat", sans-serif;
  }
  .letterhead {
    position: absolute;
    left: 289px;
    top: 28px;
    width: 622px;
    height: 880px;
    background: var(--paper);
    box-shadow: 0 2px 10px rgba(0,0,0,0.08);
  }
  .header-bands {
    position: absolute;
    left: 0;
    top: 0;
    display: block;
  }
  .band-slate { fill: var(--slate); }
  .band-petrol { fill: var(--petrol); }
  .sender {
    position: absolute;
    left: 34px;
    top: 66px;
    padding-left: 10px;
    border-left: 2px solid var(--petrol);
    color: var(--light);
    line-height: 1.2;
  }
  .sender-name {
    font-weight: 700;
    font-size: 11px;
    letter-spacing: 0.6px;
    text-transform: uppercase;
  }
  .sender-role {
    font-weight: 300;
    font-size: 9px;
    letter-spacing: 0.3px;
  }
  .company-name {
    position: absolute;
    left: 300px;
    top: 26px;
    color: var(--light);
    font-weight: 300;
    font-size: 13px;
    letter-spacing: 1px;
    text-transform: uppercase;
    white-space: nowrap;
  }
  .footer {
    position: absolute;
    right: 18px;
    bottom: 20px;
    text-align: right;
    color: var(--ink);
    font-size: 6.5px;
    line-height: 1.5;
    letter-spacing: 0.2px;
  }
  .footer-label {
    color: var(--petrol);
    font-weight: 700;
  }
</style>
</head>
<body>
  <main class="letterhead">
    <svg class="header-bands" width="622" height="110" viewBox="0 0 622 110" aria-hidden="true">
      <polygon class="band-slate" points="0,0 248,0 272,110 0,110"/>
      <polygon class="band-petrol" points="258,0 622,0 622,66 272.4,66"/>
    </svg>
    <div class="sender">
      <p class="sender-name">Helen Marlowe</p>
      <p class="sender-role">Managing Director</p>
    </div>
    <p class="company-name">Marlowe Inspection Services Ltd.</p>
    <footer class="footer">
      <p>The Willows, Mill Lane, Ashcombe, Hartford, Wessex, HT4 7QR</p>
      <p><span class="footer-label">Phone:</span> +07700 900418 &nbsp;<span class="footer-label">Email:</span> helen@marlowe-mail.co.uk · Company registration No. 08452671</p>
    </footer>
  </main>
</body>
</html>
```